Mortgage Map Flyer / Email Design

To create a one page document / email that shows a map / road map of the Mortgage Process

Client decides to Purchase a Home
Client find a reputable lenders, typically online or through a trusted friend / resource
Sets an appointment to either meet with that Lender / Loan officer in person, or speaks on the phone
Review credit and borrower documents
Pre Qualification so we stay within the budget of the client or a plan is put in place to help borrower qualify for the purchase they are seeking
Find a trust Realtor to search for homes
Tour homes to find the right fit for the client and their family
Make an offer
Ratify the contract & sign loan disclosures
Go into underwriting
Loan Approval
Sign final loan documents
Fund and move in!

Target Market(s)

Clients looking to purchase a home

Industry/Entity Type

Mortgage

Font styles to use
Sans Serif

Requirements
Must have
• Pictures, road map or map with arrows pointing the way through the process. Want to have something I can print, or embed in an email
Nice to have
• Looking to have similar colors and feel as our branch website, with our loan process videos at www.rlkhome.example
• Our logo and colors would be obviously nice to tie in as well!

```html
<!DOCTYPE html>
<html lang="en">
<head>
<meta charset="utf-8">
<title>Mortgage Process Map</title>
<link href="https://fonts.googleapis.com/css2?family=Fira+Sans+Condensed:ital,wght@0,400;0,600;0,700;0,800;1,600;1,700&family=Josefin+Sans:wght@300&family=Fira+Sans:wght@400;600&display=swap" rel="stylesheet">
<style>
  :root {
    --sky: #27a7e0;
    --arrow: #2aa3dc;
    --orange: #f9a93a;
    --ink: #1d1d1d;
    --paper: #ffffff;
    --card-light: #f2f2f2;
    --card-dark: #c9c9c9;
  }
  * { box-sizing: border-box; margin: 0; padding: 0; }
  html, body { width: 1200px; height: 1200px; overflow: hidden; background: #fff; }
  .flyer {
    position: absolute; left: 135px; top: 0;
    width: 930px; height: 1200px;
    background: var(--paper);
    box-shadow: 0 0 8px rgba(0,0,0,0.25);
    overflow: hidden;
    font-family: "Fira Sans Condensed", sans-serif;
    color: var(--ink);
  }
  .header { position: absolute; left: 0; top: 0; width: 930px; height: 180px; }
  .title {
    position: absolute; left: 0; top: 18px; width: 930px;
    text-align: center; color: #fff;
    font-weight: 800; font-size: 78px; letter-spacing: 0.5px; line-height: 1;
  }
  .route { position: absolute; left: 0; top: 0; width: 930px; height: 1200px; }
  .step {
    position: absolute; width: 180px; height: 191px;
    border-radius: 12px;
    background: radial-gradient(ellipse at 50% 50%, var(--card-light) 0%, #e2e2e2 55%, var(--card-dark) 100%);
    box-shadow: 2px 3px 4px rgba(0,0,0,0.35);
    display: flex; align-items: center; justify-content: center;
    text-align: center; text-transform: uppercase;
    font-size: 16.5px; line-height: 26.5px; font-weight: 400;
  }
  .step.small { font-size: 14px; line-height: 26.5px; }
  .step.tight { font-size: 14px; line-height: 24.3px; padding-top: 4px; }
  .step b { font-weight: 700; }
  .badge {
    position: absolute; top: -13px; right: -20px;
    width: 47px; height: 47px; border-radius: 50%;
    background: var(--orange); border: 3px solid #fff;
    box-shadow: 0 1px 3px rgba(0,0,0,0.3);
    color: #fff; font-weight: 800; font-size: 31px; line-height: 41px; text-align: center;
  }
  .badge.left { right: auto; left: -28px; top: -7px; }
  .row1 { top: 190px; } .row2 { top: 394px; } .row3 { top: 724px; }
  .c1 { left: 45px; } .c2 { left: 265px; } .c3 { left: 485px; } .c4 { left: 707px; }
  .brand { position: absolute; left: 23px; top: 984px; width: 240px; text-align: center; }
  .brand-mark { width: 44px; height: 44px; background: #1d1d1d; margin: 0 auto 14px; }
  .brand-name { font-family: "Josefin Sans", sans-serif; font-weight: 300; font-size: 18px; letter-spacing: 2.5px; text-transform: uppercase; }
  .contact-cta { font-weight: 700; font-style: italic; font-size: 16px; margin-top: 10px; }
  .contact-line { font-family: "Fira Sans", sans-serif; font-size: 13.5px; letter-spacing: 1.2px; line-height: 18px; }
  .fine-print { font-size: 8px; text-transform: uppercase; line-height: 11px; margin-top: 12px; }
  .home-art { position: absolute; left: 305px; top: 984px; width: 193px; height: 165px; }
  .move-line {
    position: absolute; left: 680px; top: 1028px; width: 300px; margin-left: -150px; text-align: center;
    font-family: "Fira Sans", sans-serif; font-weight: 600; font-style: italic;
    font-size: 44px; letter-spacing: 3px; line-height: 48px; text-transform: uppercase;
  }
  .footer-band { position: absolute; left: 0; bottom: 0; width: 930px; height: 19px; background: var(--sky); }
</style>
</head>
<body>
<main class="flyer">
  <svg class="header" viewBox="0 0 930 180" aria-hidden="true">
    <polygon points="0,0 930,0 930,175 465,107 0,175" fill="var(--sky)"/>
  </svg>
  <h1 class="title">MORTGAGE PROCESS MAP</h1>

  <svg class="route" viewBox="0 0 930 1200" aria-hidden="true">
    <defs>
      <pattern id="arrow-right" width="10.5" height="12" patternUnits="userSpaceOnUse">
        <polygon points="0,1 9,6 0,11 3,6" fill="var(--arrow)"/>
      </pattern>
      <pattern id="arrow-left" width="10.5" height="12" patternUnits="userSpaceOnUse">
        <polygon points="10,1 1,6 10,11 7,6" fill="var(--arrow)"/>
      </pattern>
      <pattern id="arrow-down" width="12" height="10.5" patternUnits="userSpaceOnUse">
        <polygon points="1,0 6,9 11,0 6,3" fill="var(--arrow)"/>
      </pattern>
    </defs>
    <rect x="19" y="176" width="12" height="236" fill="url(#arrow-down)"/>
    <rect x="21" y="411" width="886" height="12" fill="url(#arrow-right)"/>
    <rect x="901" y="418" width="12" height="260" fill="url(#arrow-down)"/>
    <rect x="21" y="677" width="886" height="12" fill="url(#arrow-left)"/>
    <rect x="17" y="684" width="12" height="256" fill="url(#arrow-down)"/>
    <rect x="21" y="940" width="886" height="12" fill="url(#arrow-right)"/>
    <rect x="901" y="947" width="12" height="204" fill="url(#arrow-down)"/>
    <rect x="682" y="1151" width="225" height="12" fill="url(#arrow-left)"/>
  </svg>

  <div class="step row1 c1"><span>Client decides<br>to <b>purchase</b><br><b>a home</b></span><div class="badge">1</div></div>
  <div class="step small row1 c2"><span>Client find a<br><b>reputable lenders,</b><br>typically online or<br>through a trusted<br>friend / resource</span><div class="badge">2</div></div>
  <div class="step small row1 c3"><span>Sets an <b>appointment</b> to<br>either meet with that<br>lender / loan officer<br>in person, or speaks<br>on the phone</span><div class="badge">3</div></div>
  <div class="step row1 c4"><span>Review <b>credit</b><br>and borrower<br>documents</span><div class="badge">4</div></div>

  <div class="step tight row2 c1"><span><b>Pre qualification</b><br>so we stay within the<br>budget of the client<br>or a plan is put in place<br>to help borrower<br>qualify for the purchase<br>they are seeking</span><div class="badge left">5</div></div>
  <div class="step row2 c2"><span>Find a <b>trust</b><br><b>realtor</b> to<br>search for<br>homes</span><div class="badge left">6</div></div>
  <div class="step row2 c3"><span>Tour homes to<br>find the <b>right fit</b><br>for the client<br>and their family</span><div class="badge left">7</div></div>
  <div class="step row2 c4"><span>Make an<br><b>offer</b></span><div class="badge left">8</div></div>

  <div class="step row3 c1"><span>Ratify the<br><b>contract &amp;</b><br><b>sign loan</b><br>disclosures</span><div class="badge">9</div></div>
  <div class="step row3 c2"><span>Go into<br><b>underwriting</b></span><div class="badge">10</div></div>
  <div class="step row3 c3"><span>Loan<br><b>approval</b></span><div class="badge">11</div></div>
  <div class="step row3 c4"><span><b>Sign final</b><br>loan documents</span><div class="badge">12</div></div>

  <div class="brand">
    <div class="brand-mark"></div>
    <div class="brand-name">Ridgeline Bank</div>
    <div class="contact-cta">CONTACT US TODAY!</div>
    <div class="contact-line">555-014-2290</div>
    <div class="contact-line">WWW.RLKHOME.EXAMPLE</div>
    <div class="fine-print">Ridgeline Bank N.A. - Mortgage Division<br>NMLS #000000</div>
  </div>

  <svg class="home-art" viewBox="0 0 193 165" role="img" aria-label="Orange line drawing of a house with a four-pane window">
    <rect x="0" y="0" width="193" height="165" rx="6" fill="#fde9cb"/>
  </svg>
  <svg class="route" viewBox="0 0 930 1200" aria-hidden="true" style="pointer-events:none">
    <line x1="305" y1="1158" x2="682" y2="1158" stroke="var(--orange)" stroke-width="3"/>
  </svg>

  <p class="move-line">Fund and<br>move in!</p>
  <div class="footer-band"></div>
</main>
</body>
</html>
```